MoneyCompass.net Site Redesign

We are looking to redesign our MoneyCompass.net site. This site is focused on helping consumers make smart financial decisions. We provide reviews and articles in various categories.

We are looking for a responsive design to run on wordpress. We will also have promoslot advertisements on our page and will want some ad spot space. We are thinking of two column design vs. single column.

Here is an example of what our competitors look like:
BuyerBeacon.org (mostly reviews vs. articles)
Homepage - https://www.buyerbeacon.org/
Category Review Listing - https://www.buyerbeacon.org/mortgage-refinance/best-mortgage-refinance
Individual Review - https://www.buyerbeacon.org/mortgage-refinance/c/harbor-vale-mortgage-refinance-review

- I like that the site is extremely clean. I like the fixed header in mobile

PlumGuide
Homepage - https://www.plumguide.example/
Category Review Listing-https://www.plumguide.example/auto_insurance/index.php
Individual Review- https://www.plumguide.example/auto_insurance/rovaro_review.php

Articles - https://www.plumguide.example/blog/2017/11/20/going-on-a-holiday-road-trip-be-prepared-for-these-hazards/

What I Like? I like the two column layout in that it gives room for advertising.
What I Do NOT Like? The top navigation is a little cumbersome and old. Mobile view is not very good. Content seems a bit cluttered.

TallyKite
Homepage - https://www.tallykite.example
Category Review Listing - https://www.tallykite.example/blog/insurance/best-car-insurance-companies/?trk=tk_gn1_4.0
Individual Review- https://www.tallykite.example/blog/insurance/brevona-insurance-review/

What I Like? very clean. Like the use of white space and focus on bright color call to action buttons.
What I Do NOT Like? In mobile a lot of content is pushed below the fold because of the large image above the fold. Reviews are not well organized.

Target Market(s)

consumers interested in saving money and making smart financial decisions

Industry/Entity Type

Financial

Logo Text

MoneyCompass.net or MoneyCompass

Coding

Coded - Design and coding required

Number of Pages Required

5+ page

Font styles to use
Sans Serif

Colors

Designer to choose colors to be used in the design.

Requirements
Must have
• -responsive design
• -room for ad space in the right column
Nice to have
• -good use of white space
• -clean layouts
Should not have
• -clutter

```html
<!DOCTYPE html>
<html lang="en">
<head>
<meta charset="utf-8">
<title>MoneyCompass.net — Make smarter financial decisions</title>
<link rel="stylesheet" href="https://fonts.googleapis.com/css2?family=Lato:wght@400;700;900&display=swap">
<style>
  :root {
    --brand-blue: #1b74b5;
    --navy: #14306b;
    --link-blue: #1f6fb8;
    --orange: #ee6a14;
    --ink: #2a2a2a;
    --text: #444;
    --muted: #5a5a5a;
    --panel: #efefef;
    --white: #fff;
    --footer: #1a78b8;
    --footer-bar: #2e2e2e;
  }
  * { box-sizing: border-box; margin: 0; padding: 0; }
  html, body { width: 1200px; height: 2258px; overflow: hidden; }
  body { font-family: "Lato", Arial, sans-serif; color: var(--text); background: var(--white); }
  a { color: inherit; text-decoration: none; }
  .wrap { width: 1050px; margin: 0 auto; position: relative; }

  /* Header */
  .site-header { height: 98px; background: var(--white); }
  .site-header .wrap { height: 98px; display: flex; align-items: center; }
  .brand { display: flex; align-items: center; gap: 10px; font-weight: 900; font-size: 22px; color: var(--brand-blue); letter-spacing: -0.2px; }
  .brand-mark { width: 30px; height: 30px; background: var(--brand-blue); }
  .category-menu { margin-left: 26px; font-size: 14px; font-weight: 700; color: #333; display: flex; align-items: center; gap: 10px; }
  .category-menu svg { width: 10px; height: 8px; }
  .main-nav { display: flex; gap: 24px; margin-left: 50px; font-size: 14px; font-weight: 700; color: #333; letter-spacing: 0.3px; }
  .btn { display: inline-block; background: var(--orange); color: var(--white); font-weight: 700; text-transform: uppercase; text-align: center; letter-spacing: 0.3px; }
  .btn-login { margin-left: auto; width: 160px; height: 36px; line-height: 36px; font-size: 14px; }

  /* Hero */
  .hero { height: 385px; position: relative; text-align: center; color: var(--white); overflow: hidden; }
  .hero-photo { position: absolute; inset: 0; background: linear-gradient(100deg, #6a6763 0%, #4f4a46 35%, #5b4a47 55%, #8a8480 80%, #a9a6a3 100%); }
  .hero-shade { position: absolute; inset: 0; background: rgba(20, 20, 20, 0.35); }
  .hero-content { position: relative; padding-top: 92px; }
  .hero-title { font-size: 51px; font-weight: 900; line-height: 1; letter-spacing: -0.3px; }
  .hero-sub { font-size: 20px; font-weight: 700; letter-spacing: 0.6px; margin-top: 8px; }
  .search-pill { width: 570px; height: 52px; margin: 14px auto 0; background: var(--white); border-radius: 26px; box-shadow: 0 0 0 4px rgba(40, 40, 40, 0.55); font-size: 26px; line-height: 52px; color: #222; font-weight: 700; }
  .search-pill span { color: #8a8a8a; }
  .disclosure { margin-top: 20px; font-size: 15px; font-weight: 700; }
  .disclosure a { color: #4aa3f0; text-decoration: underline; font-weight: 400; }

  /* Category tiles */
  .categories { height: 454px; background: var(--panel); padding-top: 44px; }
  .tile-grid { display: grid; grid-template-columns: repeat(4, 252px); grid-auto-rows: 176px; column-gap: 14px; row-gap: 17px; }
  .tile { position: relative; display: flex; align-items: center; justify-content: center; color: var(--white); font-size: 19px; font-weight: 700; text-shadow: 0 1px 3px rgba(0,0,0,0.6); }
  .tile::after { content: ""; position: absolute; inset: 0; background: rgba(0,0,0,0.22); }
  .tile span { position: relative; z-index: 1; }
  .tile-refinance { background: linear-gradient(135deg, #3d5a7a, #a88f8a); }
  .tile-loans { background: linear-gradient(135deg, #8b6a55, #5b4a40); }
  .tile-alerts { background: linear-gradient(135deg, #cfd8dc, #8fa6b1); }
  .tile-security { background: linear-gradient(180deg, #27456e, #4a5566 70%, #3b3b3b); }
  .tile-reverse { background: linear-gradient(135deg, #cfc8bd, #5c554c); }
  .tile-pet { background: linear-gradient(180deg, #7a7a60, #4d6a32); }
  .tile-dental { background: linear-gradient(135deg, #9ed0d6, #3e7d8a); }
  .tile-credit { background: linear-gradient(135deg, #d6d6d6, #4e4a48); }

  /* Editorial process */
  .editorial { height: 343px; background: var(--white); text-align: center; }
  .section-title { font-size: 28px; font-weight: 700; color: var(--ink); padding-top: 24px; }
  .process { display: flex; justify-content: space-between; width: 1080px; margin: 38px auto 0; }
  .process-step { width: 360px; }
  .process-icon { width: 92px; height: 92px; margin: 0 auto; border: 3px solid var(--navy); border-radius: 50%; display: flex; align-items: center; justify-content: center; }
  .process-icon svg { width: 36px; height: 36px; fill: var(--navy); }
  .process-step h3 { font-size: 19px; font-weight: 700; color: var(--ink); margin-top: 22px; }
  .process-step p { font-size: 16px; line-height: 25px; color: var(--muted); margin: 4px auto 0; width: 300px; }

  /* Guides */
  .guides { height: 587px; background: var(--panel); padding-top: 38px; }
  .guides-head { display: flex; justify-content: space-between; align-items: center; }
  .guides-title { font-size: 27px; font-weight: 700; color: var(--ink); letter-spacing: 0.2px; }
  .carousel-arrows { display: flex; gap: 14px; }
  .carousel-arrows svg { width: 14px; height: 20px; stroke: #333; stroke-width: 3; fill: none; }
  .article-grid { display: grid; grid-template-columns: repeat(3, 330px); column-gap: 30px; margin-top: 22px; }
  .article-image { height: 184px; }
  .img-cash { background: linear-gradient(135deg, #e8e6dc, #a9a58f 60%, #ece8d6); }
  .img-moto { background: linear-gradient(180deg, #3d5a2a 0%, #7d8f4a 45%, #9b9b8f 75%, #8f8f86 100%); }
  .img-policy { background: linear-gradient(135deg, #f2f2f0, #d8d8d4 60%, #8c7a5a); }
  .article-title { font-size: 21px; font-weight: 700; color: var(--ink); line-height: 26px; margin-top: 18px; min-height: 52px; }
  .byline { display: flex; align-items: center; gap: 14px; margin-top: 10px; font-size: 15px; color: #333; }
  .avatar { width: 30px; height: 30px; border-radius: 50%; background: #9c9c9c; }
  .excerpt { font-size: 15.5px; line-height: 25.5px; color: var(--muted); margin-top: 12px; }
  .excerpt a { color: var(--link-blue); font-weight: 700; }
  .btn-more { display: block; width: 160px; height: 35px; line-height: 35px; font-size: 14px; margin: 40px auto 0; }

  /* Footer */
  .site-footer { height: 335px; background: var(--footer); color: var(--white); padding-top: 54px; }
  .footer-cols { display: flex; }
  .footer-col h4 { font-size: 16px; font-weight: 700; margin-bottom: 8px; }
  .footer-col ul { list-style: none; font-size: 14px; line-height: 28.6px; }
  .col-all { width: 428px; }
  .col-all .lists { display: flex; gap: 0; }
  .col-all ul:first-child { width: 178px; }
  .col-popular { width: 287px; }
  .col-disclosure { width: 335px; }
  .col-disclosure p { font-size: 14px; line-height: 23px; width: 330px; }
  .follow { margin-top: 28px; }
  .social { display: flex; gap: 22px; margin-top: 14px; }
  .social span { width: 22px; height: 22px; border-radius: 50%; background: var(--white); }
  .footer-bar { height: 56px; background: var(--footer-bar); color: #bbb; font-size: 13px; }
  .footer-bar .wrap { height: 56px; display: flex; align-items: center; justify-content: space-between; }
</style>
</head>
<body>

<header class="site-header">
  <div class="wrap">
    <a class="brand" href="#"><span class="brand-mark"></span>MoneyCompass.net</a>
    <div class="category-menu">All Categories
      <svg viewBox="0 0 10 8"><path d="M0 0h10L5 8z" fill="#333"/></svg>
    </div>
    <nav class="main-nav">
      <a href="#">CREDIT CARDS</a><a href="#">BANKING</a><a href="#">INVESTING</a><a href="#">MORTGAGES</a>
    </nav>
    <a class="btn btn-login" href="#">Join or Login</a>
  </div>
</header>

<section class="hero">
  <div class="hero-photo" role="img" aria-label="Couple smiling at a laptop in a bright home office"></div>
  <div class="hero-shade"></div>
  <div class="hero-content">
    <h1 class="hero-title">Make smarter financial decisions</h1>
    <p class="hero-sub">FIND THE BEST FINANCIAL PRODUCTS &amp; SERVICES</p>
    <div class="search-pill">I'm looking for <span>product and category</span></div>
    <p class="disclosure">Disclosure: We receive advertising revenue from some partners. <a href="#">Learn more</a></p>
  </div>
</section>

<section class="categories">
  <div class="wrap tile-grid">
    <a class="tile tile-refinance" href="#" role="img" aria-label="Hands around a piggy bank"><span>Mortgage Refinance</span></a>
    <a class="tile tile-loans" href="#" role="img" aria-label="Shoppers on a city street"><span>Personal Loans</span></a>
    <a class="tile tile-alerts" href="#" role="img" aria-label="Two smiling healthcare workers"><span>Medical Alerts</span></a>
    <a class="tile tile-security" href="#" role="img" aria-label="Modern house at dusk"><span>Home Security</span></a>
    <a class="tile tile-reverse" href="#" role="img" aria-label="Reverse mortgage form with a pen"><span>Reverse Mortgages</span></a>
    <a class="tile tile-pet" href="#" role="img" aria-label="Small dog sitting on grass"><span>Pet Insurance</span></a>
    <a class="tile tile-dental" href="#" role="img" aria-label="Patient in a dental chair"><span>Dental Insurance</span></a>
    <a class="tile tile-credit" href="#" role="img" aria-label="Woman holding a credit card at a laptop"><span>Credit Repair</span></a>
  </div>
</section>

<section class="editorial">
  <h2 class="section-title">Our Editorial Process</h2>
  <div class="process">
    <div class="process-step">
      <div class="process-icon"><svg viewBox="0 0 24 24"><path d="M3 3h2v16h16v2H3z"/><rect x="7" y="11" width="2.5" height="6"/><rect x="11" y="7" width="2.5" height="10"/><rect x="15" y="9" width="2.5" height="8"/><rect x="19" y="5" width="2" height="12"/></svg></div>
      <h3>We Analyze &amp; Explain</h3>
      <p>We analyze &amp; explain how each online service works.</p>
    </div>
    <div class="process-step">
      <div class="process-icon"><svg viewBox="0 0 24 24"><path d="M5 2h9l5 5v15H5zM13 3v5h5z"/><rect x="8" y="11" width="8" height="1.6" fill="#fff"/><rect x="8" y="14" width="8" height="1.6" fill="#fff"/><rect x="8" y="17" width="8" height="1.6" fill="#fff"/></svg></div>
      <h3>We Test &amp; Compare</h3>
      <p>We test &amp; compare the leading services in each category</p>
    </div>
    <div class="process-step">
      <div class="process-icon"><svg viewBox="0 0 24 24"><rect x="2" y="10" width="4" height="11"/><path d="M8 10l4-8c1.5 0 2.5 1 2.2 3L13.5 9H20c1.2 0 2 1 1.8 2.2l-1.5 8C20 20.3 19.2 21 18 21H8z"/></svg></div>
      <h3>We Review &amp; Rate</h3>
      <p>We review and rate each service to show which is best</p>
    </div>
  </div>
</section>

<section class="guides">
  <div class="wrap">
    <div class="guides-head">
      <h2 class="guides-title">GUIDES &amp; ARTICLES FROM OUR EDITORS</h2>
      <div class="carousel-arrows">
        <svg viewBox="0 0 14 20"><path d="M11 2L3 10l8 8"/></svg>
        <svg viewBox="0 0 14 20"><path d="M3 2l8 8-8 8"/></svg>
      </div>
    </div>
    <div class="article-grid">
      <article class="article-card">
        <div class="article-image img-cash" role="img" aria-label="Roll of banknotes held by a rubber band"></div>
        <h3 class="article-title">5 “Easy” Ways Parents Can Save $1000’s a Year</h3>
        <div class="byline"><span class="avatar"></span>By Dana Whitfield</div>
        <p class="excerpt">Parents, let’s face it – the high cost of raising children leaves us all needing a little extra money. Short of getting a big raise, switching jobs, or winning... <a href="#">Read More</a></p>
      </article>
      <article class="article-card">
        <div class="article-image img-moto" role="img" aria-label="Two riders on a motorcycle on a country road"></div>
        <h3 class="article-title">Motorcycle Insurance Basics</h3>
        <div class="byline"><span class="avatar"></span>By Dana Whitfield</div>
        <p class="excerpt">Motorcycle insurance can be quite expensive; it can be the same amount as an auto insurance quote in some cases. Depending on the coverage you select and your driving... <a href="#">Read More</a></p>
      </article>
      <article class="article-card">
        <div class="article-image img-policy" role="img" aria-label="Auto insurance policy with car key and cash"></div>
        <h3 class="article-title">How Do I Get Cheap Auto Insurance?</h3>
        <div class="byline"><span class="avatar"></span>By Dana Whitfield</div>
        <p class="excerpt">If you’re looking for cheap auto insurance, then you aren’t alone. Many drivers regularly search for lower cost, more affordable insurance for their vehicles on a regular basis. If...... <a href="#">Read More</a></p>
      </article>
    </div>
    <a class="btn btn-more" href="#">More Articles</a>
  </div>
</section>

<footer class="site-footer">
  <div class="wrap footer-cols">
    <div class="footer-col col-all">
      <h4>All Services Reviewed</h4>
      <div class="lists">
        <ul><li>Annuities</li><li>Auto Insurance</li><li>Credit Monitoring</li><li>Credit Repair</li><li>Debt Management</li><li>Homeowners Insurance</li><li>Identity Theft</li><li>Life Insurance</li></ul>
        <ul><li>Mortgages</li><li>Online Brokerages</li><li>Payday Loans</li><li>Personal Finance</li><li>Student Loan Consolidation</li><li>Tax Settlement</li></ul>
      </div>
    </div>
    <div class="footer-col col-popular">
      <h4>Popular Services Reviewed</h4>
      <ul><li>Debt Management</li><li>Payday Loans</li><li>Credit Cards</li></ul>
    </div>
    <div class="footer-col col-disclosure">
      <h4>Advertising Disclosure:</h4>
      <p>MoneyCompass.net is an independent advertising supported comparison service. MoneyCompass.net may be compensated in exchange for featured placement of certain sponsored products and services, or your clicking on links posted on this website.</p>
      <h4 class="follow">Follow Us</h4>
      <div class="social"><span></span><span></span><span></span><span></span><span></span></div>
    </div>
  </div>
</footer>
<div class="footer-bar">
  <div class="wrap">
    <span>Copyright © 2018 MoneyCompass. All rights reserved.</span>
    <span>About us / Privacy Policy / Terms of Service / Contact us</span>
  </div>
</div>

</body>
</html>
```